Stationary Package for Construction Company
Harborline Construction & Development, LLC
Stationary Package for Construction Company - Construction
Creative Brief
Bright & Fun-filled
Kevin R. Tolliver
Partner
1587 Marlow Avenue, STE 210 Myrtle Beach, SC 29577
kevin@harborlinehomebuilders.example
www.harborlinehomebuilders.example
travelkq travelkq

```html
<!DOCTYPE html>
<html lang="en">
<head>
<meta charset="utf-8">
<title>Harborline Construction &amp; Development – Business Card</title>
<link rel="stylesheet" href="https://fonts.googleapis.com/css2?family=Montserrat:wght@400;500;600&display=swap">
<style>
  :root {
    --page: #ffffff;
    --card-edge: #2a2a2a;
    --ink-dark: #101010;
    --brand-red: #ec1c24;
    --light: #ffffff;
    --muted-ink: #3a3a3a;
  }
  * { box-sizing: border-box; margin: 0; padding: 0; }
  html, body {
    width: 1200px; height: 751px; overflow: hidden;
    background: var(--page);
    font-family: "Montserrat", Arial, sans-serif;
  }
  .business-card {
    position: absolute; left: 72px; top: 72px;
    width: 1056px; height: 605px;
    border: 2px solid var(--card-edge);
    overflow: hidden;
  }
  .card-backdrop { position: absolute; inset: 0; width: 100%; height: 100%; }
  .brand-lockup {
    position: absolute; left: 58px; top: 255px;
    display: flex; align-items: center; gap: 16px;
  }
  .brand-mark {
    width: 86px; height: 86px; border-radius: 50%;
    border: 5px solid var(--brand-red); flex: none;
  }
  .brand-name {
    font-size: 46px; font-weight: 600; letter-spacing: 3px;
    color: var(--muted-ink); line-height: 1;
  }
  .brand-tagline {
    margin-top: 8px; font-size: 13.5px; font-weight: 500;
    color: var(--muted-ink); letter-spacing: 0.5px;
  }
  .contact-name {
    position: absolute; left: 641px; top: 92px;
    font-size: 31px; font-weight: 400; color: var(--light);
  }
  .name-accent {
    position: absolute; left: 1014px; top: 78px;
    width: 40px; height: 42px; background: var(--brand-red);
  }
  .contact-list { position: absolute; left: 641px; top: 0; list-style: none; }
  .contact-item {
    position: absolute; left: 0; display: flex; align-items: center;
    gap: 20px; white-space: nowrap;
  }
  .contact-icon {
    width: 36px; height: 36px; border-radius: 50%;
    background: var(--light); display: flex; align-items: center; justify-content: center;
    flex: none;
  }
  .contact-icon svg { width: 20px; height: 20px; }
  .contact-text { font-size: 17px; line-height: 22px; color: var(--light); }
</style>
</head>
<body>
  <div class="business-card">
    <svg class="card-backdrop" viewBox="0 0 1056 605" preserveAspectRatio="none" aria-hidden="true">
      <rect width="1056" height="605" fill="var(--ink-dark)"/>
      <path d="M0 0 L571 0 Q662 300 516 605 L0 605 Z" fill="var(--brand-red)"/>
      <path d="M0 0 L533 0 Q632 300 485 605 L0 605 Z" fill="var(--page)"/>
    </svg>

    <div class="brand-lockup">
      <span class="brand-mark"></span>
      <div>
        <div class="brand-name">HARBORLINE</div>
        <div class="brand-tagline">CONSTRUCTION AND DEVELOPMENT</div>
      </div>
    </div>

    <div class="contact-name">Kevin R. Tolliver</div>
    <div class="name-accent"></div>

    <ul class="contact-list">
      <li class="contact-item" style="top:296px">
        <span class="contact-icon"><svg viewBox="0 0 24 24"><path d="M12 2a7 7 0 0 0-7 7c0 5 7 13 7 13s7-8 7-13a7 7 0 0 0-7-7zm0 9.5A2.5 2.5 0 1 1 12 6.5a2.5 2.5 0 0 1 0 5z" fill="var(--ink-dark)"/></svg></span>
        <span class="contact-text">1587 Marlow Avenue, STE 210<br>Myrtle Beach, SC 29577</span>
      </li>
      <li class="contact-item" style="top:345px">
        <span class="contact-icon"><svg viewBox="0 0 24 24"><path d="M6.6 10.8a15 15 0 0 0 6.6 6.6l2.2-2.2a1 1 0 0 1 1-.25 11.4 11.4 0 0 0 3.6.57 1 1 0 0 1 1 1V20a1 1 0 0 1-1 1A17 17 0 0 1 3 4a1 1 0 0 1 1-1h3.5a1 1 0 0 1 1 1c0 1.25.2 2.45.57 3.57a1 1 0 0 1-.25 1z" fill="var(--ink-dark)"/></svg></span>
        <span class="contact-text">843.555.0147<br>843.555.0182</span>
      </li>
      <li class="contact-item" style="top:393px">
        <span class="contact-icon"><svg viewBox="0 0 24 24"><rect x="6" y="3" width="12" height="6" fill="var(--ink-dark)"/><rect x="3" y="10" width="18" height="10" rx="1.5" fill="var(--ink-dark)"/><rect x="7" y="13" width="10" height="2" fill="var(--light)"/></svg></span>
        <span class="contact-text">866.555.0139</span>
      </li>
      <li class="contact-item" style="top:441px">
        <span class="contact-icon"><svg viewBox="0 0 24 24"><rect x="3" y="5" width="18" height="14" rx="1.5" fill="var(--ink-dark)"/><path d="M4 6.5l8 6 8-6" fill="none" stroke="var(--light)" stroke-width="1.6"/></svg></span>
        <span class="contact-text">kevin@harborlinehomebuilders.example</span>
      </li>
      <li class="contact-item" style="top:491px">
        <span class="contact-icon"><svg viewBox="0 0 24 24" fill="none" stroke="var(--ink-dark)" stroke-width="1.8"><circle cx="12" cy="12" r="9"/><ellipse cx="12" cy="12" rx="4" ry="9"/><path d="M3 12h18M4.5 7.5h15M4.5 16.5h15"/></svg></span>
        <span class="contact-text">www.harborlinehomebuilders.example</span>
      </li>
    </ul>
  </div>
</body>
</html>
```